Life Coach for Lawyers Business Card Design

Elegant, original, business card design for life coaching service for associate attorneys who work in big law and struggle with stress, overwhelm, and time management. Double sided design.

Target Market(s)

Women associate attorneys who work in big law and struggle with stress, overwhelm, and time management.

Industry/Entity Type

Life Coaching

Contact Information for Business Card

Marissa Pendrell
Life Coach
518.677.3941
calmbriefcounsel.net
marissa@calmbriefcounsel.net
@calmbriefcounsel (Snapline)

Font styles to use
Other font styles liked:
• Silver South font duo. See uploaded files.

Requirements
Must have
• Icons for phone, website, email, and Snapline instead of words. Specific colors used in my logo (171B2B, 421121, FFFFFF)
Nice to have
• Foil. Embossed. Feminine design.
Should not have
• Any colors other than those used in logo. See uploaded files.

```html
<!DOCTYPE html>
<html lang="en">
<head>
<meta charset="utf-8">
<title>Calm Brief Counsel – Business Card</title>
<link rel="stylesheet" href="https://fonts.googleapis.com/css2?family=Cormorant+Garamond:wght@400;500;600&family=Allison&display=swap">
<style>
  :root {
    --navy: #171B2B;
    --plum: #421121;
    --white: #FFFFFF;
    --stage: #e8e5e2;
    --rule: rgba(23, 27, 43, 0.25);
  }
  * { margin: 0; padding: 0; box-sizing: border-box; }
  html, body { width: 1200px; height: 1000px; overflow: hidden; }
  body {
    background: var(--stage);
    font-family: "Cormorant Garamond", Georgia, serif;
    position: relative;
  }
  .card {
    position: absolute;
    left: 250px;
    width: 700px;
    height: 400px;
    border-radius: 4px;
    box-shadow: 0 10px 28px rgba(23, 27, 43, 0.22);
    overflow: hidden;
  }
  /* ---------- Front ---------- */
  .card--front {
    top: 70px;
    background: linear-gradient(35deg, var(--plum) 0%, #2f1628 45%, var(--navy) 100%);
    display: flex;
    align-items: center;
    justify-content: center;
    gap: 22px;
  }
  .front-mark {
    width: 46px;
    height: 46px;
    border: 2px solid var(--white);
    border-radius: 50%;
  }
  .front-name {
    color: var(--white);
    font-weight: 500;
    font-size: 40px;
    letter-spacing: 0.14em;
    text-transform: uppercase;
  }
  /* ---------- Back ---------- */
  .card--back {
    top: 530px;
    background: var(--white);
    color: var(--navy);
  }
  .back-brand {
    position: absolute;
    left: 170px;
    top: 58px;
    color: var(--plum);
    font-weight: 600;
    font-size: 30px;
    letter-spacing: 0.08em;
    text-transform: uppercase;
  }
  .rule {
    position: absolute;
    height: 1px;
    background: var(--rule);
  }
  .rule--brand { left: 440px; right: 0; top: 120px; }
  .rule--title { left: 200px; right: 0; top: 222px; }
  .rule--contact { left: 0; width: 470px; top: 282px; }
  .holder-name {
    position: absolute;
    left: 150px;
    top: 160px;
    font-family: "Allison", cursive;
    font-size: 54px;
    line-height: 1;
    color: var(--plum);
  }
  .holder-title {
    position: absolute;
    left: 222px;
    top: 228px;
    font-weight: 600;
    font-size: 15px;
    letter-spacing: 0.12em;
    color: var(--navy);
  }
  .contact-list {
    position: absolute;
    list-style: none;
    font-size: 14px;
    color: var(--navy);
  }
  .contact-list li {
    display: flex;
    align-items: center;
    gap: 12px;
    height: 30px;
  }
  .contact-list--social { left: 455px; top: 160px; }
  .contact-list--direct { left: 90px; top: 292px; }
  .icon { width: 16px; height: 16px; flex: none; }
  .icon--dot {
    width: 14px; height: 14px;
    border-radius: 50%;
    background: var(--plum);
  }
</style>
</head>
<body>

  <section class="card card--front" aria-label="Card front">
    <span class="front-mark" aria-hidden="true"></span>
    <span class="front-name">Calm Brief Counsel</span>
  </section>

  <section class="card card--back" aria-label="Card back">
    <div class="back-brand">Calm Brief Counsel</div>
    <div class="rule rule--brand"></div>

    <div class="holder-name">Marissa Pendrell</div>
    <div class="rule rule--title"></div>
    <div class="holder-title">LIFE COACH</div>

    <ul class="contact-list contact-list--social">
      <li>
        <svg class="icon" viewBox="0 0 16 16" aria-hidden="true">
          <path d="M8 1a5 5 0 0 0-5 5c0 3.8 5 9 5 9s5-5.2 5-9a5 5 0 0 0-5-5z" fill="var(--plum)"/>
          <circle cx="8" cy="6" r="1.8" fill="var(--white)"/>
        </svg>
        your business location
      </li>
      <li><span class="icon icon--dot" aria-hidden="true"></span>your snapline handle</li>
      <li><span class="icon icon--dot" aria-hidden="true"></span>your chirpwire handle</li>
    </ul>

    <div class="rule rule--contact"></div>

    <ul class="contact-list contact-list--direct">
      <li>
        <svg class="icon" viewBox="0 0 16 16" aria-hidden="true">
          <rect x="4" y="1" width="8" height="14" rx="1.5" fill="none" stroke="var(--plum)" stroke-width="1.4"/>
          <line x1="7" y1="12.5" x2="9" y2="12.5" stroke="var(--plum)" stroke-width="1.2"/>
        </svg>
        your phone number
      </li>
      <li>
        <svg class="icon" viewBox="0 0 16 16" aria-hidden="true">
          <circle cx="8" cy="8" r="2.6" fill="none" stroke="var(--plum)" stroke-width="1.5"/>
          <path d="M10.6 5.5v3.6c0 1.3 2.6 1.6 2.9-.6A5.6 5.6 0 1 0 11 13" fill="none" stroke="var(--plum)" stroke-width="1.5" stroke-linecap="round"/>
        </svg>
        marissa@calmbriefcounsel.net
      </li>
      <li>
        <svg class="icon" viewBox="0 0 16 16" aria-hidden="true">
          <circle cx="8" cy="8" r="6.5" fill="none" stroke="var(--plum)" stroke-width="1.4"/>
          <ellipse cx="8" cy="8" rx="2.8" ry="6.5" fill="none" stroke="var(--plum)" stroke-width="1.1"/>
          <line x1="1.5" y1="8" x2="14.5" y2="8" stroke="var(--plum)" stroke-width="1.1"/>
        </svg>
        calmbriefcounsel.net
      </li>
    </ul>
  </section>

</body>
</html>
```